Consultancy Business Card Design

We need a business card design for a new company based in singapore called FortyOne. FortyOne a boutique consultancy firm offering broad-based business solutions, from conception to re-invention, for ventures from new start-ups to long-running traditional businesses.
Its 2 main divisions (Food & Beverage Operations and Construction & Project Management) have access to a wide range of networks, knowledge bases, and resources to service its clients across numerous diverse sectors. This includes, and is not limited to, construction, F&B, and retail.
We are a company that combines the ambition, boldness and energy of one in the 20s with the dedication, level-headedness and dependability of one entering its 30s. Bridging the experiences of the old with ideals of the young, we draw on the positives of both to create a unique synergy.
We hope to see designs that fits our company profile.
Boutique
Contact Information for Business Card
FortyOne(Company Name)
Marcus Tan (Name)
Principle Consultant (Title)
F&B and Hospitality (Division)
(+65) 8364 5107 (Contact no.)
marcus@fortyone-example.com.sg (Email)
Colors
Designer to choose colors to be used in the design.

```html
<!DOCTYPE html>
<html lang="en">
<head>
<meta charset="utf-8">
<title>FortyOne Business Card</title>
<link rel="stylesheet" href="https://fonts.googleapis.com/css2?family=Arimo:wght@400&display=swap">
<style>
  :root {
    --backdrop: #d6d6d6;
    --card: #313131;
    --band-dark: #3d3d3d;
    --accent: #a81e23;
    --accent-bright: #e0262b;
    --text-light: #ffffff;
    --text-soft: #dcdcdc;
  }
  html, body {
    margin: 0;
    padding: 0;
    width: 900px;
    height: 1200px;
    overflow: hidden;
    background: var(--backdrop);
    font-family: "Arimo", Arial, sans-serif;
  }
  .canvas {
    position: relative;
    width: 900px;
    height: 1200px;
  }
  .card {
    position: absolute;
    left: 154px;
    width: 562px;
    height: 346px;
    background: var(--card);
    overflow: hidden;
  }
  .card--front { top: 185px; }
  .card--back { top: 689px; }
  .wordmark {
    position: absolute;
    left: 0;
    width: 100%;
    margin: 0;
    text-align: center;
    font-size: 61px;
    font-weight: 400;
    letter-spacing: -1px;
    line-height: 1;
    color: var(--text-light);
  }
  .card--front .wordmark { top: 138px; }
  .card--back .wordmark { top: 78px; }
  .person {
    position: absolute;
    right: 307px;
    top: 208px;
    text-align: right;
    color: var(--text-soft);
  }
  .person__name {
    margin: 0 0 5px;
    font-size: 20px;
    font-weight: 400;
    line-height: 24px;
  }
  .person__role {
    margin: 0;
    font-size: 12.5px;
    line-height: 19px;
  }
  .divider {
    position: absolute;
    left: 278px;
    top: 193px;
    width: 1px;
    height: 93px;
    background: var(--accent);
  }
  .contact {
    position: absolute;
    left: 303px;
    top: 219px;
    margin: 0;
    padding: 0;
    list-style: none;
    color: var(--text-soft);
    font-size: 12.5px;
    line-height: 20px;
  }
  .band {
    position: absolute;
    bottom: 0;
    height: 11px;
  }
  .band--dark { left: 0; width: 405px; background: var(--band-dark); }
  .band--accent { left: 405px; width: 157px; background: var(--accent); }
</style>
</head>
<body>
<main class="canvas">
  <section class="card card--front" aria-label="Card front">
    <h1 class="wordmark">FortyOne</h1>
  </section>

  <section class="card card--back" aria-label="Card back">
    <p class="wordmark">FortyOne</p>
    <div class="person">
      <h2 class="person__name">Marcus Tan</h2>
      <p class="person__role">Principle Consultant</p>
      <p class="person__role">F&amp;B and Hospitality</p>
    </div>
    <div class="divider"></div>
    <ul class="contact">
      <li>(+65) 8364 5107</li>
      <li>marcus@fortyone-example.com.sg</li>
    </ul>
    <div class="band band--dark"></div>
    <div class="band band--accent"></div>
  </section>
</main>
</body>
</html>
```